Letterhead for a German Distribution/Manufacturing Company

We need a professional Letterhead in a unique Design.
not to playful.
The Letterhead has to show show that we are a international company with headquater in Germany.
all details like adress, Vat Tax Number, Bank Accout, Eori, email, Company number has to be on the Letterhead.
for example use: VAT TAX DE5704168 Bank Account: Norrfeld Bank IBAN DE421705238ß310482 Swift: KOLV3154802 EORI 3041296587 Company Number: HRB 61508 Adress: VOLTRINA UG Amsel Strasse 7 Postal Code 04683 City Kessbrück Country: Germany Email: info@voltrina-example.com
the design can be colored but doesnt have to be
Industry/Entity Type
Manufacturing and international distribution
Requirements
Must have
- show that we are a international company with headquater in Germany. our company infos and logo

```html
<!DOCTYPE html>
<html lang="en">
<head>
<meta charset="utf-8">
<title>VOLTRINA Letterhead</title>
<link href="https://fonts.googleapis.com/css2?family=Figtree:wght@400;600&display=swap" rel="stylesheet">
<style>
  :root {
    --backdrop: #e9e9e9;
    --paper: #ffffff;
    --ink: #1e1e1e;
    --corner: #3d3d3d;
    --rule: #b5b5b5;
    --ghost: #f2f2f2;
  }
  * { margin: 0; padding: 0; box-sizing: border-box; }
  html, body {
    width: 1200px; height: 1200px; overflow: hidden;
    background: var(--backdrop);
    font-family: "Figtree", Arial, sans-serif;
    color: var(--ink);
  }
  .letterhead {
    position: absolute; left: 211px; top: 50px;
    width: 777px; height: 1100px;
    background: var(--paper);
    box-shadow: 4px 4px 6px rgba(0,0,0,0.35);
    overflow: hidden;
  }
  .corner { position: absolute; }
  .corner--top { right: 0; top: 0; }
  .corner--bottom { left: 0; bottom: 0; }
  .brand {
    position: absolute; left: 42px; top: 52px;
    display: flex; align-items: center; gap: 10px;
  }
  .brand__dot {
    width: 26px; height: 26px; border-radius: 50%;
    background: var(--corner);
  }
  .brand__name {
    font-size: 33px; font-weight: 400; letter-spacing: 0.5px;
    color: var(--ink); line-height: 1;
  }
  .brand-ghost {
    position: absolute; left: 0; right: 0; top: 505px;
    display: flex; justify-content: center; align-items: center; gap: 20px;
  }
  .brand-ghost__dot {
    width: 78px; height: 78px; border-radius: 50%; background: var(--ghost);
  }
  .brand-ghost__name {
    font-size: 84px; font-weight: 400; color: var(--ghost); line-height: 1;
    letter-spacing: 1px;
  }
  .footer {
    position: absolute; left: 97px; width: 587px; top: 973px;
    border-top: 1px solid var(--rule);
    padding-top: 10px;
    display: grid;
    grid-template-columns: 214px 266px 1fr;
    row-gap: 12px;
    font-size: 10.5px; line-height: 1.3;
  }
  .footer__item { white-space: nowrap; }
  .footer__label { font-weight: 600; display: block; }
</style>
</head>
<body>
  <main class="letterhead">
    <svg class="corner corner--top" width="154" height="148" viewBox="0 0 154 148" aria-hidden="true">
      <polygon points="0,0 154,0 154,148" fill="var(--corner)"/>
    </svg>
    <svg class="corner corner--bottom" width="115" height="88" viewBox="0 0 115 88" aria-hidden="true">
      <polygon points="0,0 115,88 0,88" fill="var(--corner)"/>
    </svg>

    <header class="brand">
      <span class="brand__dot"></span>
      <span class="brand__name">VOLTRINA</span>
    </header>

    <div class="brand-ghost" aria-hidden="true">
      <span class="brand-ghost__dot"></span>
      <span class="brand-ghost__name">VOLTRINA</span>
    </div>

    <footer class="footer">
      <div class="footer__item"><span class="footer__label">VAT TAX</span>DE5704168</div>
      <div class="footer__item"><span class="footer__label">Bank Account</span>Norrfeld Bank IBAN DE421705238ß310482</div>
      <div class="footer__item"><span class="footer__label">Company Number</span>HRB 61508</div>
      <div class="footer__item"><span class="footer__label">Address</span>VOLTRINA UG Amsel Strasse 7 Postal<br>Code 04683 City Kessbrück Germany</div>
      <div class="footer__item"><span class="footer__label">Swift</span>KOLV3154802 EORI 3041296587</div>
      <div class="footer__item"><span class="footer__label">Email</span>info@voltrina-example.com</div>
    </footer>
  </main>
</body>
</html>
```